Silver Brook Constructions Ltd Stationary
business cards, stationary etc.
Silver Brook Constructions Ltd Stationary - Construction
Creative Brief
Simple
Dalton Wexford
4816 Ardmore Rd. Cedar Falls N.R. V8N 4K7
250-384-6252 could we put this number under office instead of phone
222-222-2222 temporary until I get new number
dalton@silverbrookconstructions.example
www.silverbrookconstructions.example
We would like designs for business cards , envelopes, letterhead, thank-you cards with evelopes, fax cover sheet, and presentation folder. Thank you
information should be on the back of the card along with some clean lines and simplicity while keeping a very professional feel

```html
<!DOCTYPE html>
<html lang="en">
<head>
<meta charset="utf-8">
<title>Silver Brook Constructions Ltd — Business Card</title>
<link rel="stylesheet" href="https://fonts.googleapis.com/css2?family=Cinzel:wght@600&family=Tinos:wght@400;700&display=swap">
<style>
  :root {
    --backdrop: #1e1e20;
    --card-light: #ffffff;
    --card-dark: #030303;
    --ink-dark: #3a3a3a;
    --ink-muted: #5f5f5f;
    --ink-light: #f2f2f2;
    --mark-ring: #8d9aa0;
    --mark-fill: #dfe6e8;
  }
  html, body {
    margin: 0;
    padding: 0;
    width: 1200px;
    height: 809px;
    overflow: hidden;
    background: var(--backdrop);
  }
  .canvas {
    position: relative;
    width: 1200px;
    height: 809px;
  }
  .card {
    position: absolute;
    width: 552px;
    height: 314px;
    border-radius: 20px;
    box-sizing: border-box;
  }
  .card-front {
    left: 163px;
    top: 108px;
    background: var(--card-light);
    text-align: center;
  }
  .brand-dot {
    position: absolute;
    left: 50%;
    top: 24px;
    width: 92px;
    height: 92px;
    margin-left: -46px;
    border-radius: 50%;
    background: var(--mark-fill);
    border: 7px solid var(--mark-ring);
    box-sizing: border-box;
  }
  .brand-name {
    position: absolute;
    left: 0;
    right: 0;
    top: 132px;
    margin: 0;
    font-family: "Cinzel", serif;
    font-weight: 600;
    color: var(--ink-dark);
    line-height: 1.1;
  }
  .brand-name .line-main {
    display: block;
    font-size: 42px;
    letter-spacing: 1px;
  }
  .brand-name .line-sub {
    display: block;
    font-size: 17px;
    letter-spacing: 3px;
    margin-top: 2px;
  }
  .tagline {
    position: absolute;
    left: 0;
    right: 0;
    top: 218px;
    margin: 0;
    font-family: "Tinos", serif;
    font-size: 9px;
    font-weight: 700;
    letter-spacing: 2.5px;
    color: var(--ink-muted);
    text-transform: uppercase;
  }
  .card-back {
    left: 542px;
    top: 413px;
    background: var(--card-dark);
    color: var(--ink-light);
    font-family: "Tinos", serif;
  }
  .person-name {
    position: absolute;
    left: 19px;
    top: 48px;
    margin: 0;
    font-size: 24px;
    font-weight: 700;
  }
  .contact {
    position: absolute;
    left: 19px;
    margin: 0;
    font-size: 13px;
    line-height: 18px;
    font-style: normal;
  }
  .address { top: 118px; }
  .phones { top: 196px; }
  .website {
    position: absolute;
    left: 19px;
    top: 280px;
    margin: 0;
    font-size: 13px;
    line-height: 18px;
  }
  .back-dot {
    position: absolute;
    left: 353px;
    top: 206px;
    width: 74px;
    height: 74px;
    border-radius: 50%;
    background: var(--mark-fill);
    border: 5px solid var(--mark-ring);
    box-sizing: border-box;
  }
</style>
</head>
<body>
  <main class="canvas">
    <section class="card card-front" aria-label="Business card front">
      <div class="brand-dot"></div>
      <h1 class="brand-name">
        <span class="line-main">Silver Brook</span>
        <span class="line-sub">Constructions Ltd.</span>
      </h1>
      <p class="tagline">Building with lasting care</p>
    </section>

    <section class="card card-back" aria-label="Business card back">
      <h2 class="person-name">Dalton Wexford</h2>
      <address class="contact address">
        4816 Ardmore Rd.<br>
        Cedar Falls N.R.<br>
        V8N 4K7
      </address>
      <p class="contact phones">
        O : 250.384.6252<br>
        C : 222-222-2222<br>
        E : dalton@silverbrookconstructions.example
      </p>
      <p class="website">www.silverbrookconstructions.example</p>
      <div class="back-dot"></div>
    </section>
  </main>
</body>
</html>
```